RMV Halvora BANK Website Design with UX/UI

I need a website DEV Design Mock up that can be presented in full HTML. Not code needed...just clickable design.
This is a BANk website.
We wil send some websites we like a bit later.
We need at least 10 pages that are Full HTML and integrated.
I will send more Design requirement details.
but feel free to go for it and be ahead

Hi
This is a Bank.
It will be based in the Caribbean. Please read up a bit about the Caribbean so you appreciate our region.
Therefore the only ethnicity that can be used is African American. Go to snapmeadow and search African American People so you can see the ethnicity of the people whom you must feature

The colour Scheme will be those of the Logo. The pantones were provided but it is the BLUE and Yellowish Orange

Target Market(s)

All Bank Customers

Industry/Entity Type

Banking

Number of Pages Required

5+ page

Colors
6b449b
ffc214

Requirements
Must have
• Logo
Follow the Brand Architecture
Use the Pantones provided
Follow the Suite Map Provided
Follow the brief Attached

```html
<!DOCTYPE html>
<html lang="en">
<head>
<meta charset="utf-8">
<title>RMV Halvora Bank</title>
<link rel="stylesheet" href="https://fonts.googleapis.com/css2?family=Fira+Sans:wght@500;600;800&family=Nunito+Sans:wght@400;600;700;800&display=swap">
<style>
  :root {
    --purple: #5f3193;
    --purple-deep: #4a2377;
    --yellow: #ffc214;
    --yellow-box: #f8c40a;
    --ink: #1d1d1f;
    --text: #333;
    --light: #f4f1f2;
    --dark: #2e2e2e;
    --white: #fff;
  }
  * { box-sizing: border-box; margin: 0; padding: 0; }
  html, body { width: 1200px; height: 2994px; overflow: hidden; }
  body { position: relative; font-family: "Nunito Sans", sans-serif; color: var(--text); background: var(--white); }
  .abs { position: absolute; }
  .heading { font-family: "Fira Sans", sans-serif; font-weight: 600; color: var(--ink); letter-spacing: .5px; }
  .btn { position: absolute; display: flex; align-items: center; justify-content: center; border-radius: 4px; font-weight: 800; font-size: 13px; letter-spacing: .3px; text-transform: uppercase; background: var(--yellow); color: var(--ink); }
  .rule { position: absolute; height: 3px; width: 46px; background: var(--yellow); }
  .para { position: absolute; font-size: 15.5px; line-height: 19.3px; }

  /* header */
  .topbar { top: 0; left: 0; width: 1200px; height: 41px; background: var(--light); }
  .topnav { position: absolute; top: 14px; left: 320px; display: flex; font-size: 11.5px; color: #333; }
  .topnav span { padding: 0 8px; border-right: 1px solid #d8d3d6; line-height: 14px; }
  .topnav span:first-child { padding-left: 0; }
  .topnav span:last-child { border: none; }
  .search { position: absolute; top: 7px; left: 908px; width: 159px; height: 27px; background: #fff; border: 1px solid #d5d0d3; border-radius: 6px; font-size: 10px; color: #777; padding: 6px 9px; }
  .search i { position: absolute; right: 5px; top: 4px; width: 17px; height: 17px; border-radius: 50%; background: var(--yellow); }
  .mainnav { top: 41px; left: 0; width: 1200px; height: 64px; background: #fff; }
  .mainnav ul { list-style: none; position: absolute; top: 27px; left: 321px; display: flex; gap: 19px; font-size: 12.5px; color: #222; }
  .mainnav li.active { color: var(--purple); font-weight: 800; }
  .brand-badge { position: absolute; top: -9px; left: 113px; width: 178px; height: 178px; border-radius: 50%; background: #fff; display: flex; align-items: center; justify-content: center; z-index: 5; }
  .brand-name { font-weight: 800; font-size: 22px; color: var(--purple); text-align: center; line-height: 1.1; }

  /* hero */
  .hero { top: 105px; left: 0; width: 1200px; height: 534px; background: linear-gradient(100deg, #6a5a55 0%, #8a6e66 30%, #a57c78 50%, #6d4c43 75%, #3f3a3a 100%); }
  .hero h1 { position: absolute; top: 172px; left: 131px; font-family: "Fira Sans", sans-serif; font-weight: 800; font-size: 67px; color: #fff; letter-spacing: 1px; }
  .hero p { position: absolute; top: 258px; left: 134px; font-size: 22px; line-height: 26px; color: #fff; font-weight: 600; }
  .dots { position: absolute; top: 492px; left: 565px; display: flex; gap: 10px; }
  .dots i { width: 7px; height: 7px; border-radius: 50%; background: #fff; }
  .dots i.on { background: var(--yellow); }

  /* product cards */
  .card { position: absolute; top: 677px; width: 300px; height: 172px; border-radius: 6px; overflow: hidden; }
  .card .fill { position: absolute; inset: 0; }
  .card .shade { position: absolute; left: 0; right: 0; bottom: 0; height: 70px; background: linear-gradient(transparent, rgba(0,0,0,.8)); }
  .card b { position: absolute; left: 15px; bottom: 13px; color: #fff; font-size: 13px; font-weight: 800; letter-spacing: .4px; }
  .card .arrow { position: absolute; right: 8px; bottom: 8px; width: 19px; height: 19px; border-radius: 3px; background: var(--yellow); }

  /* welcome */
  .welcome { top: 886px; left: 0; width: 1200px; height: 425px; background: var(--light); }
  .welcome .photo { position: absolute; right: 0; top: 0; width: 700px; height: 425px; background: linear-gradient(90deg, var(--light) 0%, #cfd3d4 25%, #bfc5c8 60%, #a8b0b4 100%); }
  .tag { position: absolute; top: 61px; left: 132px; background: var(--purple); color: #fff; font-family: "Fira Sans", sans-serif; font-weight: 600; font-size: 18px; padding: 3px 9px; }

  /* investments purple */
  .invest { top: 1311px; left: 0; width: 1200px; height: 484px; background: var(--purple); }
  .invest .frame { position: absolute; left: 178px; top: 82px; width: 405px; height: 351px; background: var(--yellow); }
  .invest .photo { position: absolute; left: 185px; top: 54px; width: 413px; height: 373px; background: linear-gradient(140deg, #6f8a4c 0%, #4b6a35 45%, #35332f 100%); }

  /* investments yellow */
  .feature { top: 1795px; left: 0; width: 1200px; height: 482px; background: #fff; }
  .feature .photo { position: absolute; left: 535px; top: 64px; width: 533px; height: 356px; background: linear-gradient(90deg, #cfd6db 0%, #e9ecee 50%, #d8dde1 100%); }
  .feature .box { position: absolute; left: 131px; top: 128px; width: 473px; height: 238px; background: var(--yellow-box); }

  /* apply */
  .apply { top: 2277px; left: 0; width: 1200px; height: 326px; background: linear-gradient(90deg, #2d2d2d, #3a3a3a 60%, #303030); }

  /* footer */
  .footer { top: 2603px; left: 0; width: 1200px; height: 391px; background: var(--light); }
  .footer h4 { position: absolute; font-size: 14px; font-weight: 800; color: var(--ink); letter-spacing: .3px; }
  .footer .uline { position: absolute; height: 1px; background: var(--purple); }
  .footer ul { position: absolute; list-style: none; font-size: 12px; line-height: 19.2px; color: #333; text-transform: uppercase; }
  .social { position: absolute; left: 905px; display: flex; align-items: center; gap: 14px; font-size: 14.5px; line-height: 19px; color: #222; }
  .social i { width: 28px; height: 28px; border-radius: 50%; background: var(--purple); }
  .footer .divider { position: absolute; top: 307px; left: 131px; width: 937px; height: 1px; background: #d9d4d7; }
  .copy { position: absolute; top: 342px; left: 0; width: 1200px; text-align: center; font-size: 12px; color: #333; }
</style>
</head>
<body>

<header>
  <div class="abs topbar">
    <nav class="topnav">
      <span>HELP &amp; SUPPORT</span><span>CAREERS</span><span>CHECKING</span><span>SAVINGS</span><span>CREDIT CARDS</span><span>MORTGAGES</span><span>INVESTMENTS</span>
    </nav>
    <div class="search">I'm looking for<i></i></div>
  </div>
  <div class="abs mainnav">
    <ul>
      <li class="active">PERSONAL</li><li>SMALL BUSINESS</li><li>PRIVATE BANKING</li><li>CORPORATE</li><li>WEALTH</li><li>ONILNE BANKING</li><li>ATM &amp; BRANCH</li><li>LOANS</li>
    </ul>
  </div>
  <div class="brand-badge"><div class="brand-name">RMV<br>Halvora</div></div>
</header>

<section class="abs hero" role="img" aria-label="Piggy bank on a wooden desk with a laptop and plant behind">
  <h1>SAVINGS</h1>
  <p>Lorem Ipsum is simply dummy text of the<br>printing and typesetting.</p>
  <div class="btn" style="top:338px;left:131px;width:140px;height:44px;font-size:15px;border-radius:5px;">Read More</div>
  <div class="dots"><i></i><i></i><i class="on"></i><i></i><i></i></div>
</section>

<div class="card" style="left:131px">
  <div class="fill" role="img" aria-label="Blue car driving on a coastal road at sunset" style="background:linear-gradient(120deg,#4a5a6a,#8a8470 50%,#e8c88a)"></div>
  <div class="shade"></div><b>VEHICLE LOANS</b><span class="arrow"></span>
</div>
<div class="card" style="left:450px">
  <div class="fill" role="img" aria-label="Hands stacking wooden blocks into a house shape" style="background:linear-gradient(120deg,#c9d6e2,#e8e2da 50%,#d8b890)"></div>
  <div class="shade"></div><b>MORTGAGES</b><span class="arrow"></span>
</div>
<div class="card" style="left:768px">
  <div class="fill" role="img" aria-label="Stack of payment cards" style="background:linear-gradient(120deg,#8a8a86,#b8a06a 45%,#3e4650)"></div>
  <div class="shade"></div><b>CREDIT CARDS</b><span class="arrow"></span>
</div>

<section class="abs welcome">
  <div class="photo" role="img" aria-label="Smiling businessman in shirt and tie in a bright office"></div>
  <div class="tag">WELCOME TO</div>
  <h2 class="heading abs" style="top:98px;left:132px;font-size:30px;">RMV HALVORA BANK</h2>
  <div class="rule" style="top:141px;left:132px;"></div>
  <p class="para" style="top:178px;left:132px;width:350px;">Lorem ipsum dolor sit amet, consectetur adipi scing elit, sed do eiusmod tempor incididunt ut labore et dolore magna aliqua. Ut enim ad minim veniam, quis nostrud exercitation ulla mco laboris nisi ut aliquip ex ea commodo consequat. Duis aute irure dolor in repreh enderit in voluptate.</p>
  <div class="btn" style="top:328px;left:136px;width:111px;height:36px;">Read More</div>
</section>

<section class="abs invest">
  <div class="frame"></div>
  <div class="photo" role="img" aria-label="Father carrying his smiling son outdoors among trees"></div>
  <h2 class="heading abs" style="top:83px;left:656px;font-size:29px;color:#fff;">INVESTMENTS</h2>
  <div class="rule" style="top:128px;left:658px;"></div>
  <p class="para" style="top:170px;left:658px;width:345px;color:#fff;">Lorem ipsum dolor sit amet, consectetur adipi scing elit, sed do eiusmod tempor incididunt ut labore et dolore magna aliqua. Ut enim ad minim veniam, quis nostrud exercitation ulla mco laboris nisi ut aliquip ex ea commodo consequat. Duis aute irure dolor in repreh enderit in voluptate.</p>
  <div class="btn" style="top:323px;left:661px;width:111px;height:36px;">Read More</div>
</section>

<section class="abs feature">
  <div class="photo" role="img" aria-label="Smiling woman leaning on a desk using a tablet"></div>
  <div class="box">
    <h2 class="heading abs" style="top:35px;left:46px;font-size:29px;">INVESTMENTS</h2>
    <div class="rule" style="top:77px;left:46px;background:var(--purple);"></div>
    <p class="para" style="top:110px;left:47px;width:360px;">Lorem ipsum dolor sit amet, consectetur adipi scing elit, sed do eiusmod tempor incididunt ut labore et dolore magna aliqua. Ut enim ad minim veniam, quis nostrud exercitation ull.</p>
  </div>
  <div class="btn" style="top:351px;left:181px;width:112px;height:36px;background:var(--purple);color:#fff;">Read More</div>
</section>

<section class="abs apply" role="img" aria-label="Dimmed photo of a piggy bank on a desk">
  <h2 class="heading abs" style="top:58px;left:0;width:1200px;text-align:center;font-size:29px;color:#fff;">INSTANT APPLY</h2>
  <div class="rule" style="top:108px;left:577px;"></div>
  <p class="para" style="top:141px;left:320px;width:560px;text-align:center;color:#eee;line-height:21px;">Lorem ipsum dolor sit amet, consectetur adipi scing elit, sed do eiusmod tempor incididunt ut labore et dolore magna aliqua. Ut enim ad minim veniam, quis nostrud exercitation ulla mco laboris nisi ut aliquip ex ea commodo consequat.</p>
  <div class="btn" style="top:238px;left:544px;width:112px;height:35px;">Apply Now</div>
</section>

<footer class="abs footer">
  <div class="abs brand-name" style="top:85px;left:131px;width:170px;font-size:30px;">RMV<br>Halvora</div>

  <h4 style="top:53px;left:379px;">MENU</h4>
  <div class="uline" style="top:77px;left:379px;width:259px;"></div>
  <ul style="top:103px;left:379px;">
    <li>Personal</li><li>Small Business</li><li>Private Banking</li><li>Corporate</li><li>Wealth</li><li>Onilne Banking</li><li>ATM &amp; Branch</li><li>Loans</li>
  </ul>
  <ul style="top:103px;left:543px;">
    <li>Help &amp; Support</li><li>Careers</li><li>Checking</li><li>Savings</li><li>Credit Cards</li><li>Mortgages</li><li>Investments</li>
  </ul>

  <h4 style="top:53px;left:727px;">LINKS</h4>
  <div class="uline" style="top:77px;left:727px;width:66px;"></div>
  <ul style="top:103px;left:728px;">
    <li>Privacy</li><li>Mortgages</li><li>Contact Us</li><li>Sitemap</li>
  </ul>

  <h4 style="top:53px;left:908px;">FOLLOW US</h4>
  <div class="uline" style="top:77px;left:908px;width:80px;"></div>
  <div class="social" style="top:104px;"><i></i><span>Like us on<br>FRIENDLANE</span></div>
  <div class="social" style="top:164px;"><i></i><span>Follow us on<br>CHIRPNET</span></div>
  <div class="social" style="top:225px;"><i></i><span>Follow us on<br>WORKFOLD</span></div>

  <div class="divider"></div>
  <p class="copy">Copyright © 2020 All Rights Reserved</p>
</footer>

</body>
</html>
```